Business Card Design Project

I am community manager and social media strategist. I need a double sided business card with company logo and name. Looking for something professional, elegant but also a little bit original.

• - The logo and the colours are the company colours and a required to stay.
- The size should be: 84 x 55 mm (or 3.30 x 2.16)
- The file size should be: 1039 x 697 pixels (300 dpi)
- I'd like rounded corners. :)

Use the following contact information for the card:

Léonie Vardin
Stratégie médias sociaux / community management / édition de sites sociaux
mob. : 0687529103
leonie.vardin@postelune.fr
Pépie. : @lvardin
Appel : vardin.leonie

```html
<!DOCTYPE html>
<html lang="fr">
<head>
<meta charset="utf-8">
<title>AVELORA – Carte de visite</title>
<link rel="stylesheet" href="https://fonts.googleapis.com/css2?family=Ubuntu:wght@500;700&display=swap">
<style>
  :root {
    --page-bg: #e6e7e9;
    --brand-blue: #1f74d8;
    --brand-blue-deep: #0b4fb4;
    --brand-blue-light: #8fd3ff;
    --ink-blue: #2b8fe2;
    --card-white: #ffffff;
    --mist-blue: #cfe6f8;
    --mosaic-a: #3a8de6;
    --mosaic-b: #e9f2fb;
    --mosaic-c: #f0a23b;
  }
  * { box-sizing: border-box; margin: 0; padding: 0; }
  html, body { width: 1200px; height: 800px; overflow: hidden; }
  body {
    background: var(--page-bg);
    font-family: "Ubuntu", "Trebuchet MS", sans-serif;
    position: relative;
  }
  .card {
    position: absolute;
    top: 110px;
    width: 340px;
    height: 580px;
    border-radius: 44px;
    overflow: hidden;
    box-shadow: 0 8px 22px rgba(0, 0, 0, 0.18);
  }

  /* Front */
  .card-front {
    left: 235px;
    background: linear-gradient(170deg, var(--brand-blue) 0%, var(--brand-blue-deep) 100%);
    color: var(--card-white);
    text-align: center;
  }
  .brand-mark {
    width: 130px;
    height: 130px;
    margin: 48px auto 0;
    border-radius: 50%;
    background: var(--card-white);
  }
  .brand-name {
    margin-top: 26px;
    font-size: 60px;
    font-weight: 700;
    letter-spacing: 3px;
    line-height: 1;
  }
  .brand-tagline {
    margin-top: 6px;
    font-size: 29px;
    font-weight: 700;
    color: var(--brand-blue-light);
    line-height: 1;
  }
  .network-mosaic {
    position: absolute;
    left: 75px;
    bottom: 0;
    width: 200px;
    height: 220px;
    border-radius: 14px 14px 0 0;
    background: linear-gradient(160deg, var(--mosaic-a) 0%, var(--mosaic-b) 55%, var(--mosaic-c) 100%);
  }

  /* Back */
  .card-back {
    left: 625px;
    background: var(--card-white);
    color: var(--ink-blue);
  }
  .back-decoration {
    position: absolute;
    left: -120px;
    top: 190px;
    width: 360px;
    height: 360px;
  }
  .holder-name {
    position: relative;
    margin: 36px 24px 0 0;
    text-align: right;
    font-size: 38px;
    font-weight: 700;
  }
  .services {
    position: relative;
    list-style: none;
    margin: 10px 22px 0 0;
    text-align: right;
    font-size: 20px;
    font-weight: 700;
    line-height: 1.15;
  }
  .contact {
    position: absolute;
    right: 28px;
    bottom: 74px;
    font-style: normal;
    text-align: right;
    font-size: 20px;
    font-weight: 700;
    line-height: 1.2;
  }
</style>
</head>
<body>

  <section class="card card-front" aria-label="Recto">
    <div class="brand-mark"></div>
    <h1 class="brand-name">AVELORA</h1>
    <p class="brand-tagline">Community Manager</p>
    <div class="network-mosaic" role="img" aria-label="Mosaïque de pièces de puzzle aux couleurs des réseaux sociaux"></div>
  </section>

  <section class="card card-back" aria-label="Verso">
    <svg class="back-decoration" viewBox="0 0 360 360" aria-hidden="true">
      <circle cx="180" cy="180" r="170" fill="var(--mist-blue)" opacity="0.6"/>
    </svg>
    <h2 class="holder-name">Léonie Vardin</h2>
    <ul class="services">
      <li>Stratégie médias sociaux</li>
      <li>community management</li>
      <li>édition de sites sociaux</li>
    </ul>
    <address class="contact">
      <p>mob. : 0687529103</p>
      <p>leonie.vardin@postelune.fr</p>
      <p>Pépie. : @lvardin</p>
      <p>Appel : vardin.leonie</p>
    </address>
  </section>

</body>
</html>
```